Tralven Networks co-marketing flier

We want a flier that our partners (IT consultants) can hand out to their clients and that we can send to local businesses on their behalf to demonstrate that they can help customers purchase a phone system that has professional features that they would expect in a phone solution that costs thousands of dollars.

We want the brochure to look very professional with excellent layout and use of space.

The Tralven Networks corporate colour is green and more details can be found at www.tralvennetworks-example.com.au.

We have attached a draft Word document that contains most of the information we need but please present the information in the way YOU believe it should be laid out.

We are looking for a designer who understands the concept and uses their own skills to produce a work of art.

Target Market(s)

small businesses that want to save money but also want a modern phone with lots of features

Industry/Entity Type

Marketing

Requirements
Must have
• Must have an image of the main phone and a cordless handset to indicate that they don't need wires to set the system up.

Must have our logo and website address

Must have a box or some "placeholder" where our partners can stamp or insert their details.

Must have a "call to action" saying "Contact us for a quote"

```html
<!DOCTYPE html>
<html lang="en">
<head>
<meta charset="utf-8">
<title>Tralven Networks – Phone System Flier</title>
<link href="https://fonts.googleapis.com/css2?family=PT+Serif:ital,wght@1,400;1,700&family=Arimo:ital,wght@0,400;0,700;1,400;1,700&display=swap" rel="stylesheet">
<style>
  :root {
    --bg-light: #f4f4f4;
    --bg-mid: #d9d9d9;
    --teal-deep: #4fcfc0;
    --map-tone: #8fe0d6;
    --title-red: #e3171b;
    --brand-green: #3fae2a;
    --feature-green: #56c21f;
    --text-dark: #222222;
    --cloud-blue: #2f8fe6;
    --cloud-light: #8cc9f7;
    --url-blue: #2f7de1;
    --button-top: #f7f0e6;
    --button-bottom: #d7cbb9;
    --product-dark: #2c2c2c;
    --product-silver: #c9cdd1;
  }
  * { margin: 0; padding: 0; box-sizing: border-box; }
  html, body { width: 1200px; height: 848px; overflow: hidden; }
  body { font-family: "Arimo", Arial, sans-serif; background: var(--bg-light); }

  .flier {
    position: relative;
    width: 1200px;
    height: 848px;
    overflow: hidden;
    background: radial-gradient(ellipse at 40% 40%, #ffffff 0%, var(--bg-light) 45%, var(--bg-mid) 100%);
  }
  .swoosh { position: absolute; inset: 0; }

  .headline {
    position: absolute;
    left: 88px; top: 22px;
    font-family: "PT Serif", Georgia, serif;
    font-style: italic; font-weight: 700;
    font-size: 50px;
    color: var(--title-red);
    -webkit-text-stroke: 1px #ffffff;
    text-shadow: 0 0 2px #fff, 0 0 3px #fff, 2px 3px 4px rgba(0,0,0,0.45);
    letter-spacing: 0.3px;
  }
  .intro {
    position: absolute;
    left: 96px; top: 116px; width: 545px;
    font-family: "PT Serif", Georgia, serif;
    font-style: italic; font-weight: 700;
    font-size: 22px; line-height: 30px;
    letter-spacing: 0.6px;
    color: #ffffff;
    padding-left: 28px;
  }
  .intro .bullet { position: absolute; left: 0; top: 6px; }

  .world-map {
    position: absolute;
    left: 56px; top: 214px; width: 800px; height: 240px;
    background: radial-gradient(ellipse at center, var(--map-tone) 0%, rgba(143,224,214,0.25) 70%, rgba(143,224,214,0) 100%);
    border-radius: 40px;
  }

  .product-handset {
    position: absolute;
    left: 1000px; top: 28px; width: 134px; height: 226px;
    background: linear-gradient(160deg, #555 0%, var(--product-dark) 55%, #111 100%);
    border-radius: 28px 28px 20px 20px;
  }
  .product-deskphone {
    position: absolute;
    left: 42px; top: 624px; width: 346px; height: 204px;
    background: linear-gradient(170deg, var(--product-silver) 0%, #8b9096 45%, var(--product-dark) 100%);
    border-radius: 30px 60px 20px 40px;
  }

  .features {
    position: absolute;
    left: 880px; top: 283px; width: 306px; height: 318px;
    background: #ffffff;
    border-radius: 12px;
    box-shadow: 0 2px 6px rgba(0,0,0,0.12);
  }
  .features-tab {
    position: absolute;
    left: 0; top: 0; width: 176px; height: 30px;
    background: linear-gradient(90deg, var(--feature-green), #8ee04a);
    border-radius: 12px 0 0 0;
    clip-path: polygon(0 0, 88% 0, 100% 100%, 0 100%);
    color: #ffffff;
    font-style: italic; font-weight: 700;
    font-size: 17px; line-height: 30px;
    padding-left: 32px;
  }
  .features-list {
    list-style: none;
    position: absolute;
    left: 14px; top: 42px; right: 14px;
  }
  .features-list li {
    position: relative;
    padding-left: 22px;
    font-size: 16px; line-height: 19px;
    color: var(--text-dark);
    margin-bottom: 12px;
  }
  .features-list li.wrap-narrow { padding-right: 40px; }
  .features-list li::before {
    content: "";
    position: absolute; left: 0; top: 3px;
    width: 12px; height: 13px;
    background: var(--feature-green);
    clip-path: polygon(0 0, 55% 0, 100% 50%, 55% 100%, 0 100%, 30% 50%);
  }

  .cloud { position: absolute; left: 300px; top: 448px; width: 320px; height: 196px; }
  .cloud-text {
    position: absolute;
    left: 340px; top: 508px; width: 244px;
    text-align: center;
    color: #ffffff;
    font-style: italic;
    font-size: 26px; line-height: 34px;
  }

  .stamp-box {
    position: absolute;
    left: 567px; top: 651px; width: 280px; height: 180px;
    border: 1.5px solid #666;
    border-radius: 10px;
    background: linear-gradient(180deg, #f2f2f2, #e2e2e2);
  }

  .cta {
    position: absolute;
    left: 870px; top: 632px; width: 298px; height: 42px;
    border-radius: 21px;
    background: linear-gradient(180deg, var(--button-top), var(--button-bottom));
    box-shadow: inset 0 -2px 3px rgba(0,0,0,0.15), 0 1px 2px rgba(0,0,0,0.2);
    color: #555555;
    font-style: italic;
    font-size: 20px; line-height: 42px;
    text-align: center;
  }

  .brand-name {
    position: absolute;
    left: 926px; top: 710px;
    color: var(--brand-green);
    font-size: 28px; font-weight: 400;
    letter-spacing: 0.3px;
    white-space: nowrap;
  }
  .company-details {
    position: absolute;
    left: 930px; top: 759px;
    color: #111111;
    font-size: 16px; line-height: 19px;
  }
  .url-bar {
    position: absolute;
    left: 926px; top: 804px; width: 258px; height: 24px;
    border-radius: 5px;
    background: var(--url-blue);
    padding: 3px 26px 3px 4px;
  }
  .url-bar span {
    display: block;
    background: #ffffff;
    border-radius: 3px;
    height: 18px;
    font-size: 8.5px; line-height: 18px; font-weight: 700;
    font-style: italic;
    color: #222;
    padding-left: 4px;
    white-space: nowrap;
  }
  .url-bar svg { position: absolute; right: 5px; top: 4px; }
</style>
</head>
<body>
<main class="flier">

  <svg class="swoosh" width="1200" height="848" viewBox="0 0 1200 848" aria-hidden="true">
    <defs>
      <linearGradient id="tealBand" x1="0" y1="0" x2="1" y2="0.4">
        <stop offset="0" stop-color="#a6ece3"/>
        <stop offset="0.55" stop-color="#7fe0d3"/>
        <stop offset="1" stop-color="#4fcfc0"/>
      </linearGradient>
    </defs>
    <path d="M0,150 C250,80 650,50 1200,18 L1200,470 C860,470 480,540 0,665 Z" fill="url(#tealBand)"/>
    <path d="M0,150 C250,80 650,50 1200,18" fill="none" stroke="#ffffff" stroke-width="6"/>
    <path d="M0,665 C480,540 860,470 1200,470" fill="none" stroke="#ffffff" stroke-width="7"/>
  </svg>

  <div class="world-map" role="img" aria-label="Dotted world map in light teal"></div>

  <h1 class="headline">Looking for a new phone system?</h1>

  <p class="intro">
    <svg class="bullet" width="20" height="20" viewBox="0 0 20 20" aria-hidden="true">
      <circle cx="10" cy="10" r="9" fill="#ffffff"/>
      <path d="M7,5 L15,10 L7,15 Z" fill="#56c21f"/>
    </svg>
    Our proven VoIP solution comes with all the professional features to service an office of up to 6 people.
  </p>

  <div class="product-handset" role="img" aria-label="Cordless handset standing in its charging base"></div>

  <section class="features">
    <div class="features-tab">Features</div>
    <ul class="features-list">
      <li>very low line rental rates*</li>
      <li class="wrap-narrow">10c local and national calls untimed</li>
      <li>voicemail-to-email</li>
      <li>Bluetooth-to-mobile</li>
      <li>direct in-dial to every extension</li>
      <li>number portability (keep your number when you move)</li>
      <li>call records via spreadsheet</li>
      <li>flat rate local and national calls</li>
    </ul>
  </section>

  <svg class="cloud" viewBox="0 0 320 196" aria-hidden="true">
    <defs>
      <linearGradient id="cloudFill" x1="0" y1="0" x2="0" y2="1">
        <stop offset="0" stop-color="#8cc9f7"/>
        <stop offset="1" stop-color="#2f8fe6"/>
      </linearGradient>
    </defs>
    <g fill="url(#cloudFill)" stroke="#ffffff" stroke-width="3">
      <circle cx="30" cy="160" r="7"/>
      <circle cx="50" cy="150" r="10"/>
      <circle cx="78" cy="144" r="13"/>
    </g>
    <path d="M40,110 C10,105 10,60 45,62 C45,25 95,15 115,40 C130,5 195,5 205,40 C230,20 280,35 270,70 C305,75 310,125 275,128 C270,148 220,150 205,135 C185,152 125,152 110,135 C85,148 45,140 40,110 Z"
          fill="url(#cloudFill)" stroke="#ffffff" stroke-width="3"/>
  </svg>
  <p class="cloud-text">It’s Cheaper than you think !</p>

  <div class="product-deskphone" role="img" aria-label="Corded office desk phone with colour display and keypad"></div>

  <div class="stamp-box" aria-label="Space for partner details"></div>

  <div class="cta">Contact us for a Quote</div>

  <div class="brand-name">Tralven Networks</div>
  <p class="company-details">Kestrel Holdings (456 Group Pty Ltd)<br>ABN: 12 345 678 901</p>
  <div class="url-bar">
    <span>http://www.tralvennetworks-example.com.au</span>
    <svg width="16" height="16" viewBox="0 0 16 16" aria-hidden="true">
      <circle cx="9.5" cy="6.5" r="4.5" fill="none" stroke="#ffffff" stroke-width="2"/>
      <line x1="6" y1="10" x2="2" y2="14" stroke="#ffffff" stroke-width="2.5" stroke-linecap="round"/>
    </svg>
  </div>

</main>
</body>
</html>
```